Custom Real Estate Postcard for Buying Communities

We are a real estate company that owns/operates mobile home parks and want to send out a postcard to owners of these communities letting them know who our company is and let them know we want to buy their community. We are looking to create a postcard that introduces our company to the owner and also lets them know we want to buy their community - we are targeting older mom & pop type communities so we would like the postcard to have a home-y feel that makes the owner feel like our company will treat them fairly during the acquisition process
I have attached a few images from our communities that might look good on a postcard - you don't need to use all of them, I just included multiple so there are different options. please feel free to edit/enhance the images if needed.
Our company is Bright Meadow Holdings (BMH) and the logo is attached.
Text to be included somewhere on postcard: "We pride ourselves on active hands-on management in order to provide our residents quality communities at an affordable price.
BMH is a proven owner/operator and has the ability to purchase without any financing contingencies.
We provide a quick and easy closing. We do not retrade
Target Market(s)
Owners of Mobile Home Parks that BMH (our company) would like to acquire - small mom & pop owners that want to see that we aren't the big firm trying to come in and take over but a local company that will still treat the residents well
Industry/Entity Type
Real Estate
Colors
Designer to choose colors to be used in the design.
Requirements
Must have
- The BMH logo, at least one picture of a mobile home park from the attached pictures. And some version/form of the provided text. Info/contact section with website (www.bmhparks.example), email (info@bmhparks.example) and phone (555.284.7160)
- Something sort of call to action like: "We Want to Buy Your Community", "Ready to Sell?", "Interested in Selling?" etc.
Nice to have
- BMH Logo Colors, in addition to any other colors if designer thinks there are complimentary colors

```html
<!DOCTYPE html>
<html lang="en">
<head>
<meta charset="utf-8">
<title>Bright Meadow Holdings Postcard</title>
<link rel="stylesheet" href="https://fonts.googleapis.com/css2?family=Crimson+Text:wght@400;700&family=Open+Sans:wght@400;600;700&display=swap">
<style>
  :root {
    --page: #d5d5d5;
    --navy: #2e4470;
    --navy-deep: #1e3461;
    --coral: #ee7d72;
    --rust: #b1533c;
    --red: #a51d25;
    --red-dark: #c9202c;
    --white: #ffffff;
    --paper: #fbfbfb;
    --rule: #b9b9b9;
    --stamp: #d9d9d9;
    --serif: "Crimson Text", Georgia, serif;
    --sans: "Open Sans", Arial, sans-serif;
  }
  * { margin: 0; padding: 0; box-sizing: border-box; }
  html, body { width: 1047px; height: 1200px; overflow: hidden; background: var(--page); }
  .canvas { position: relative; width: 1047px; height: 1200px; }
  .postcard {
    position: absolute; left: 118px; width: 810px; height: 540px; overflow: hidden;
    box-shadow: 0 3px 10px rgba(0,0,0,.25);
  }
  .postcard--front { top: 40px; }
  .postcard--back { top: 620px; background: var(--paper); }

  /* FRONT */
  .scene-photo {
    position: absolute; inset: 0;
    background: linear-gradient(180deg, #4a8fd6 0%, #7fb5e6 18%, #6f9b4c 40%, #8ab35b 55%, #b9bcb8 64%, #9a9d9c 80%, #7fa34f 100%);
  }
  .front-panel {
    position: absolute; left: 43px; top: 0; width: 285px; height: 540px;
    background: var(--navy); color: var(--white);
    border-left: 3px solid #4f6592; border-right: 3px solid #4f6592;
  }
  .front-panel::after {
    content: ""; position: absolute; inset: 0 4px; border-left: 1px solid rgba(255,255,255,.35); border-right: 1px solid rgba(255,255,255,.35);
  }
  .logo-box {
    position: absolute; left: 24px; top: 37px; width: 228px; height: 114px;
    background: var(--white); padding: 6px;
  }
  .logo-box__inner {
    width: 100%; height: 100%; border: 2px solid var(--navy);
    display: flex; align-items: center; justify-content: center; gap: 12px;
  }
  .brand-mark { width: 30px; height: 30px; background: var(--red); flex: none; }
  .brand-name {
    font-family: var(--sans); font-weight: 600; font-size: 13px; line-height: 1.2;
    letter-spacing: 1px; text-transform: uppercase; color: var(--navy);
  }
  .headline { position: absolute; left: 0; width: 100%; text-align: center; font-family: var(--serif); text-transform: uppercase; }
  .headline--buy { top: 210px; font-size: 29px; line-height: 36px; }
  .headline--sell { top: 355px; font-size: 31px; line-height: 35px; }
  .accent { color: var(--coral); font-weight: 700; }
  .divider { position: absolute; left: 72px; top: 340px; width: 140px; height: 2px; background: rgba(255,255,255,.8); }
  .contact-list { position: absolute; left: 58px; top: 452px; list-style: none; font-family: var(--sans); font-size: 12.5px; }
  .contact-list li { display: flex; align-items: center; gap: 20px; height: 22px; }
  .contact-list svg { width: 14px; height: 14px; fill: none; stroke: var(--white); stroke-width: 1.6; }
  .fairness-ribbon { position: absolute; left: 629px; top: 0; width: 136px; height: 140px; }
  .fairness-ribbon p {
    position: absolute; inset: 12px 0 0; text-align: center; color: var(--white);
    font-family: var(--serif); font-size: 17px; line-height: 22px;
  }

  /* BACK */
  .back-panel { position: absolute; left: 0; top: 0; width: 402px; height: 540px; background: var(--navy-deep); color: var(--white); }
  .back-logo { position: absolute; left: 0; top: 36px; width: 100%; display: flex; justify-content: center; align-items: center; gap: 14px; }
  .back-logo .brand-mark { width: 40px; height: 40px; background: var(--white); }
  .back-logo .brand-name { color: var(--white); font-size: 19px; font-weight: 400; line-height: 1.15; border-left: 1px solid var(--white); padding-left: 12px; }
  .home-photo {
    position: absolute; left: 40px; top: 134px; width: 322px; height: 132px;
    border: 3px solid var(--white); box-shadow: 0 2px 6px rgba(0,0,0,.4);
    background: linear-gradient(180deg, #6f9e49 0%, #c7cfc9 40%, #e6e6e2 60%, #5e8f33 100%);
  }
  .intro-text {
    position: absolute; left: 30px; top: 283px; width: 342px; text-align: center;
    font-family: var(--sans); font-size: 12px; line-height: 22px;
  }
  .call-band { position: absolute; left: 0; top: 420px; width: 402px; height: 120px; background: var(--red); }
  .call-band__tab { position: absolute; left: 325px; top: 0; width: 77px; height: 58px; }
  .call-now {
    position: absolute; left: 50px; top: 22px; display: flex; align-items: center; gap: 10px;
    font-family: var(--sans); font-weight: 700; font-size: 17.5px; color: var(--white);
  }
  .call-now svg { width: 28px; height: 28px; }
  .web-line { position: absolute; left: 50px; top: 62px; font-family: var(--sans); font-size: 12px; color: var(--white); }
  .web-line span { margin: 0 14px; }
  .stamp-box { position: absolute; left: 634px; top: 50px; width: 106px; height: 104px; background: var(--stamp); border: 1px solid #bdbdbd; }
  .address-lines { position: absolute; left: 427px; top: 218px; width: 314px; list-style: none; }
  .address-lines li { height: 27px; border-top: 1px solid var(--rule); }
</style>
</head>
<body>
<main class="canvas">

  <section class="postcard postcard--front">
    <div class="scene-photo" role="img" aria-label="Photo of a mobile home community street with manufactured homes, green lawns, trees and a red pickup truck"></div>

    <div class="front-panel">
      <div class="logo-box">
        <div class="logo-box__inner">
          <span class="brand-mark"></span>
          <span class="brand-name">Bright Meadow<br>Holdings</span>
        </div>
      </div>
      <h1 class="headline headline--buy">We want<br>to buy your<br><span class="accent">Community</span></h1>
      <div class="divider"></div>
      <h2 class="headline headline--sell">Interested<br><span class="accent">in selling?</span></h2>
      <ul class="contact-list">
        <li><svg viewBox="0 0 16 16"><circle cx="8" cy="8" r="6.5"/><path d="M1.5 8h13M8 1.5c-3 3.5-3 9.5 0 13M8 1.5c3 3.5 3 9.5 0 13"/></svg>www.bmhparks.example</li>
        <li><svg viewBox="0 0 16 16"><rect x="1.5" y="3.5" width="13" height="9"/><path d="M1.5 3.5 8 9l6.5-5.5"/></svg>info@bmhparks.example</li>
        <li><svg viewBox="0 0 16 16"><path d="M3 2h3l1 3-2 1.5c1 2 2.5 3.5 4.5 4.5L11 9l3 1v3c-6 .5-11.5-5-11-11z"/></svg>555.284.7160</li>
      </ul>
    </div>

    <div class="fairness-ribbon">
      <svg width="136" height="140" viewBox="0 0 136 140"><path d="M0 0h136v112l-68 28L0 112z" fill="#b1533c"/></svg>
      <p>We treat you<br>with <b>fairness</b><br><b>and respect.</b></p>
    </div>
  </section>

  <section class="postcard postcard--back">
    <div class="back-panel">
      <div class="back-logo">
        <span class="brand-mark"></span>
        <span class="brand-name">Bright Meadow<br>Holdings</span>
      </div>
      <div class="home-photo" role="img" aria-label="Photo of a single-wide manufactured home with a porch, lawn and flower beds"></div>
      <p class="intro-text">We pride ourselves on active hands-on management in order to provide our residents quality communities at an affordable price. BMH is a proven owner/operator and has the ability to purchase without any financing contingencies.</p>
      <div class="call-band">
        <svg class="call-band__tab" viewBox="0 0 77 58"><path d="M0 0h77v58z" fill="#c9202c"/></svg>
        <div class="call-now">
          <svg viewBox="0 0 28 28"><circle cx="14" cy="14" r="12" fill="none" stroke="#fff" stroke-width="1.8"/><path d="M10 8h2.5l1 3-1.5 1c.8 1.7 2 2.9 3.7 3.7l1-1.5 3 1V18c-5 .4-9.9-4.6-9.7-10z" fill="none" stroke="#fff" stroke-width="1.5"/></svg>
          CALL NOW! 555.284.7160
        </div>
        <p class="web-line">www.bmhparks.example<span>|</span>Email : info@bmhparks.example</p>
      </div>
    </div>
    <div class="stamp-box"></div>
    <ul class="address-lines"><li></li><li></li><li></li><li></li><li></li><li></li><li></li></ul>
  </section>

</main>
</body>
</html>
```